Pet product line, needs a label design

We are a pharmaceutical company focused on animal health. We have been in the Mexican and Central American market for 10 years. During this time we have developed our line for production animals (beef, poultry, dairy, pigs...) and now we want to develop a line for pets.
Our first product are some pills made of Yucca (Yucca schidigera) which helps the digestive system of cats and dogs improve, reducing gas production and diminishing the bad smell of the pet feces.
We are looking for a design that can represent our new product line using this new product as an example, its name is 'VENTORAN'. The brand umbrella is BQ Vita, I am attaching this logo.
We need an attractive and original design with a strong personality, capable of jumping to the eyes of the consumer (pet owner) and also attractive for the Veterinarian who will recommend the product.
We want to highlight the benefits of the product by developing icons to the three main claims of the product.
We hope you will find this project attractive and challenging!!

Target Market(s)

Pet owners (mainly dog and cat)

Veterinarians

Industry/Entity Type

Pharmaceutical

Requirements
Must have
• * Product name (VENTORAN)
* Label Information (added in a word document)
* Band umbrella logo BQ Vita
* GREAT DESIGN
* The design should be horizontal (5cm height and 13 cm width)
Nice to have
• Nice product name design

Icon designs for the following claims (in spanish):
+ Limpia el trato digestivo (Cleans the digestive tract)
+ Reduce los malos olores (Reduces odors)
+ Propicia la digestión completa (Promotes complete digestion)

```html
<!DOCTYPE html>
<html lang="en">
<head>
<meta charset="utf-8">
<title>VENTORAN label – BQ Vita</title>
<link rel="stylesheet" href="https://fonts.googleapis.com/css2?family=Titan+One&family=Nunito:wght@700;900&display=swap">
<style>
  :root {
    --page-bg: #f1ede8;
    --green-light: #d3e2b4;
    --green-mid: #a9c489;
    --teal-title: #1f9a8f;
    --orange-light: #ffd21f;
    --orange-dark: #e07a12;
    --red-title: #e3262b;
    --title-outline: #23314f;
    --brand-blue: #2b63b0;
    --dog-tan: #c8925e;
    --dog-white: #f3ede4;
    --cat-cream: #efe4d2;
    --cat-brown: #7a6250;
    --icon-fill: #d9d7c9;
    --icon-line: #3d3d3d;
    --prohibit: #d22f2f;
  }
  * { margin: 0; padding: 0; box-sizing: border-box; }
  html, body { width: 1200px; height: 1000px; overflow: hidden; }
  body {
    background: var(--page-bg);
    display: flex;
    flex-direction: column;
    align-items: center;
    justify-content: center;
    gap: 60px;
  }
  .label {
    position: relative;
    width: 1040px;
    height: 400px;
    overflow: hidden;
    box-shadow: 0 4px 14px rgba(0,0,0,0.15);
  }
  .label--green {
    background: radial-gradient(ellipse at 55% 55%, var(--green-light), var(--green-mid));
    --title-fill: var(--teal-title);
  }
  .label--orange {
    background: radial-gradient(ellipse at 55% 60%, var(--orange-light), var(--orange-dark));
    --title-fill: var(--red-title);
  }
  .product-name {
    position: absolute;
    top: 26px;
    left: 300px;
    font-family: "Titan One", sans-serif;
    font-size: 84px;
    font-weight: 400;
    letter-spacing: 4px;
    color: var(--title-fill);
    -webkit-text-stroke: 4px var(--title-outline);
    paint-order: stroke fill;
    line-height: 1;
  }
  .brand {
    position: absolute;
    top: 120px;
    left: 40px;
    display: flex;
    align-items: center;
    gap: 12px;
    font-family: "Nunito", sans-serif;
    font-weight: 700;
    font-size: 44px;
    line-height: 1;
    color: var(--brand-blue);
  }
  .brand-mark {
    width: 30px;
    height: 30px;
    background: var(--brand-blue);
  }
  .cat-photo {
    position: absolute;
    left: 40px;
    top: 210px;
    width: 300px;
    height: 190px;
    border-radius: 90px 90px 0 0;
    background: linear-gradient(180deg, var(--cat-brown) 0%, var(--cat-brown) 30%, var(--cat-cream) 55%, var(--cat-cream) 100%);
  }
  .dog-photo {
    position: absolute;
    left: 350px;
    top: 130px;
    width: 540px;
    height: 270px;
    border-radius: 130px 130px 0 0;
    background: linear-gradient(90deg, var(--dog-tan) 0%, var(--dog-tan) 35%, var(--dog-white) 50%, var(--dog-tan) 65%, var(--dog-tan) 100%);
  }
  .claims {
    position: absolute;
    right: 30px;
    top: 23px;
    display: flex;
    flex-direction: column;
    gap: 14px;
  }
  .claim-icon {
    display: block;
    width: 78px;
    height: 78px;
  }
  .claim-icon .frame { fill: var(--icon-fill); stroke: var(--icon-line); stroke-width: 3; }
  .claim-icon .subject { fill: none; stroke: var(--icon-line); stroke-width: 3; stroke-linecap: round; stroke-linejoin: round; }
  .claim-icon .word { font-family: "Nunito", sans-serif; font-weight: 900; font-size: 13px; fill: var(--icon-line); }
  .claim-icon .no { fill: none; stroke: var(--prohibit); stroke-width: 4; }
</style>
</head>
<body>

  <section class="label label--green">
    <h1 class="product-name">VENTORAN</h1>
    <div class="brand"><span class="brand-mark"></span>BQ Vita</div>
    <div class="cat-photo" role="img" aria-label="Photo of a Burmese cat"></div>
    <div class="dog-photo" role="img" aria-label="Photo of a tan and white puppy"></div>
    <div class="claims">
      <svg class="claim-icon" viewBox="0 0 78 78" role="img" aria-label="Icon: reduces odors">
        <rect class="frame" x="3" y="3" width="72" height="72" rx="16"/>
        <path class="subject" d="M28 58c-6-8 6-12 0-20s6-12 0-18M39 58c-6-8 6-12 0-20s6-12 0-18M50 58c-6-8 6-12 0-20s6-12 0-18"/>
        <circle class="no" cx="39" cy="39" r="25"/><line class="no" x1="21" y1="21" x2="57" y2="57"/>
      </svg>
      <svg class="claim-icon" viewBox="0 0 78 78" role="img" aria-label="Icon: reduces stress">
        <rect class="frame" x="3" y="3" width="72" height="72" rx="16"/>
        <text class="word" x="39" y="44" text-anchor="middle">STRESS</text>
        <circle class="no" cx="39" cy="39" r="25"/><line class="no" x1="21" y1="21" x2="57" y2="57"/>
      </svg>
      <svg class="claim-icon" viewBox="0 0 78 78" role="img" aria-label="Icon: cleans the digestive tract">
        <rect class="frame" x="3" y="3" width="72" height="72" rx="16"/>
        <path class="subject" d="M34 18v10c0 6 14 2 16 12s-6 16-16 14-10-8-4-10"/>
        <circle class="no" cx="39" cy="39" r="25"/><line class="no" x1="21" y1="21" x2="57" y2="57"/>
      </svg>
      <svg class="claim-icon" viewBox="0 0 78 78" role="img" aria-label="Icon: promotes complete digestion">
        <rect class="frame" x="3" y="3" width="72" height="72" rx="16"/>
        <path class="subject" d="M24 48a8 8 0 0 1 4-15 11 11 0 0 1 21-2 8 8 0 0 1 5 17z"/>
        <circle class="no" cx="39" cy="39" r="25"/><line class="no" x1="21" y1="21" x2="57" y2="57"/>
      </svg>
    </div>
  </section>

  <section class="label label--orange">
    <h1 class="product-name">VENTORAN</h1>
    <div class="brand"><span class="brand-mark"></span>BQ Vita</div>
    <div class="cat-photo" role="img" aria-label="Photo of a Burmese cat"></div>
    <div class="dog-photo" role="img" aria-label="Photo of a tan and white puppy"></div>
    <div class="claims">
      <svg class="claim-icon" viewBox="0 0 78 78" role="img" aria-label="Icon: reduces odors">
        <rect class="frame" x="3" y="3" width="72" height="72" rx="16"/>
        <path class="subject" d="M28 58c-6-8 6-12 0-20s6-12 0-18M39 58c-6-8 6-12 0-20s6-12 0-18M50 58c-6-8 6-12 0-20s6-12 0-18"/>
        <circle class="no" cx="39" cy="39" r="25"/><line class="no" x1="21" y1="21" x2="57" y2="57"/>
      </svg>
      <svg class="claim-icon" viewBox="0 0 78 78" role="img" aria-label="Icon: reduces stress">
        <rect class="frame" x="3" y="3" width="72" height="72" rx="16"/>
        <text class="word" x="39" y="44" text-anchor="middle">STRESS</text>
        <circle class="no" cx="39" cy="39" r="25"/><line class="no" x1="21" y1="21" x2="57" y2="57"/>
      </svg>
      <svg class="claim-icon" viewBox="0 0 78 78" role="img" aria-label="Icon: cleans the digestive tract">
        <rect class="frame" x="3" y="3" width="72" height="72" rx="16"/>
        <path class="subject" d="M34 18v10c0 6 14 2 16 12s-6 16-16 14-10-8-4-10"/>
        <circle class="no" cx="39" cy="39" r="25"/><line class="no" x1="21" y1="21" x2="57" y2="57"/>
      </svg>
      <svg class="claim-icon" viewBox="0 0 78 78" role="img" aria-label="Icon: promotes complete digestion">
        <rect class="frame" x="3" y="3" width="72" height="72" rx="16"/>
        <path class="subject" d="M24 48a8 8 0 0 1 4-15 11 11 0 0 1 21-2 8 8 0 0 1 5 17z"/>
        <circle class="no" cx="39" cy="39" r="25"/><line class="no" x1="21" y1="21" x2="57" y2="57"/>
      </svg>
    </div>
  </section>

</body>
</html>
```